HomeBridle business card and stationary design

We are looking for a simple yet elegant design for our mortgage company business card and stationary.

The card should include:
Name (Derek Walsh)
Title (CEO)
Phone Number (614-208-3917)
Address (48 Birchfield Court, Suite 314, Marlow, OH 43952)
Email (email@homebridle-example.com)
"NMLS" i.e. (NMLS 61947)
"Company NMLS" (Company NMLS 472815)

See above

```html
<!DOCTYPE html>
<html lang="en">
<head>
<meta charset="utf-8">
<title>HomeBridle Business Card</title>
<link href="https://fonts.googleapis.com/css2?family=Figtree:wght@400;500;600;700&display=swap" rel="stylesheet">
<style>
  :root {
    --backdrop: #8a8b8c;
    --navy: #121e2a;
    --navy-ink: #14202c;
    --accent: #1591d6;
    --paper: #e7e8ea;
    --text: #1f2a35;
    --light: #eef1f4;
  }
  * { margin: 0; padding: 0; box-sizing: border-box; }
  html, body { width: 1200px; height: 781px; overflow: hidden; }
  body {
    background: var(--backdrop);
    font-family: "Figtree", Arial, sans-serif;
    position: relative;
  }
  .card {
    position: absolute;
    left: 358px;
    width: 452px;
    height: 251px;
  }
  .card-front {
    top: 104px;
    background: var(--navy);
    border-top: 7px solid var(--accent);
  }
  .card-front .wordmark {
    position: absolute;
    left: 0; right: 0;
    top: 82px;
    text-align: center;
    font-size: 50px;
    font-weight: 500;
    color: var(--light);
    letter-spacing: 0.2px;
  }
  .card-back {
    top: 408px;
    background: var(--paper);
    color: var(--text);
  }
  .card-back .wordmark {
    position: absolute;
    right: 26px;
    top: 44px;
    font-size: 30px;
    font-weight: 500;
    color: var(--navy-ink);
  }
  .contact-name {
    position: absolute;
    left: 28px;
    top: 106px;
    font-size: 16px;
    font-weight: 700;
    letter-spacing: 1.3px;
    color: var(--accent);
    text-transform: uppercase;
  }
  .contact-title {
    position: absolute;
    left: 28px;
    top: 126px;
    font-size: 13px;
  }
  .divider {
    position: absolute;
    left: 28px;
    top: 151px;
    width: 18px;
    height: 1.5px;
    background: var(--accent);
  }
  .contact-lines {
    position: absolute;
    left: 28px;
    top: 167px;
    list-style: none;
    font-size: 12.5px;
  }
  .contact-lines li {
    display: flex;
    align-items: center;
    gap: 6px;
    height: 19px;
  }
  .contact-lines svg { width: 12px; height: 12px; }
  .address {
    position: absolute;
    left: 28px;
    top: 216px;
    font-size: 12.5px;
  }
  .licences {
    position: absolute;
    right: 26px;
    top: 201px;
    text-align: right;
    font-size: 10.5px;
    line-height: 15px;
  }
</style>
</head>
<body>
  <section class="card card-front">
    <div class="wordmark">HomeBridle</div>
  </section>

  <section class="card card-back">
    <div class="wordmark">HomeBridle</div>
    <div class="contact-name">Derek Walsh</div>
    <div class="contact-title">CEO</div>
    <div class="divider"></div>
    <ul class="contact-lines">
      <li>
        <svg viewBox="0 0 24 24" fill="none" stroke="#1591d6" stroke-width="2" stroke-linejoin="round"><path d="M5 3h4l2 5-2.5 1.5a11 11 0 0 0 6 6L16 13l5 2v4a2 2 0 0 1-2 2A16 16 0 0 1 3 5a2 2 0 0 1 2-2z"/></svg>
        <span>614-208-3917</span>
      </li>
      <li>
        <svg viewBox="0 0 24 24" fill="none" stroke="#1591d6" stroke-width="2" stroke-linejoin="round"><rect x="2" y="5" width="20" height="14"/><path d="M2 5l10 8 10-8"/></svg>
        <span>email@homebridle-example.com</span>
      </li>
    </ul>
    <div class="address">48 Birchfield Court, Suite 314, Marlow, OH 43952</div>
    <div class="licences">
      <div>NMLS 61947</div>
      <div>Company NMLS 472815</div>
    </div>
  </section>
</body>
</html>
```